redesing professional certificate

Redesign our certificate to more a professional look and to make it look like a-wanna have - Best in adobe photoshop, because this template will be our basic, and we have in our education different levels, basic, upper, lower, complex, master level. I usually add a small picture to show what level they are. Or when you have a better suggestion I a gladly to hear.
We teach to physiotherapist so it has to look professional.

Target Market(s)

physiotherapist

Industry/Entity Type

Health Care

Requirements
Must have
• our logo

```html
<!DOCTYPE html>
<html lang="en">
<head>
<meta charset="utf-8">
<title>Certificate – Fascial Balance Method</title>
<link rel="stylesheet" href="https://fonts.googleapis.com/css2?family=Cinzel:wght@600&family=Noto+Serif:ital,wght@1,400;1,700&display=swap">
<style>
  :root {
    --teal-deep: #0aa8b0;
    --teal-soft: #5bb9bf;
    --navy: #1b2440;
    --gold: #f6c20c;
    --orange: #e7761b;
    --ink: #231f20;
    --paper: #ffffff;
  }
  * { margin: 0; padding: 0; box-sizing: border-box; }
  html, body { width: 848px; height: 1200px; overflow: hidden; background: var(--paper); }
  .certificate {
    position: relative; width: 848px; height: 1200px; overflow: hidden;
    background: var(--paper); color: var(--ink);
    font-family: "Noto Serif", Georgia, serif; font-style: italic;
  }
  .band { position: absolute; left: 0; width: 848px; }
  .band--top {
    top: 0; height: 290px;
    background: linear-gradient(to bottom, var(--teal-deep) 0%, var(--teal-soft) 45%, rgba(91,185,191,0) 100%);
  }
  .band--bottom {
    bottom: 0; height: 210px;
    background: linear-gradient(to bottom, rgba(246,194,12,0) 0%, var(--gold) 40%, var(--orange) 100%);
  }

  .brand-seal {
    position: absolute; left: 604px; top: 74px; width: 196px; height: 196px;
    border-radius: 50%; background: var(--navy);
    border: 5px solid var(--paper); box-shadow: 0 0 0 2px #3a3a3a;
    display: flex; align-items: center; justify-content: center; text-align: center;
  }
  .brand-seal__name { color: var(--paper); font-weight: 700; font-size: 20px; line-height: 1.25; }

  .title-ribbon { position: absolute; left: 175px; top: 303px; width: 497px; height: 67px; }
  .title-ribbon svg { position: absolute; inset: 0; }
  .title-ribbon h1 {
    position: relative; font-family: "Cinzel", "Times New Roman", serif; font-style: normal;
    font-weight: 600; font-size: 48px; letter-spacing: 6px; text-align: center;
    line-height: 67px; padding-left: 8px;
  }

  .recipient { position: absolute; top: 410px; left: 0; width: 848px; text-align: center; }
  .recipient__name { font-weight: 700; font-size: 31px; line-height: 44px; }
  .recipient__course { font-size: 22px; line-height: 31.5px; letter-spacing: 0.6px; margin-top: 4px; }

  .signatory { position: absolute; top: 604px; font-size: 22px; line-height: 32px; }
  .signatory--left { left: 157px; }
  .signatory--right { left: 552px; }

  .registration { position: absolute; left: 64px; top: 723px; font-size: 22px; letter-spacing: 0.8px; word-spacing: 4px; }
  .terms { position: absolute; left: 64px; top: 784px; font-size: 21px; line-height: 32px; white-space: nowrap; }
  .issuer { position: absolute; left: 64px; top: 916px; font-size: 22px; line-height: 32px; letter-spacing: 1.4px; font-style: italic; }
  .tagline { position: absolute; left: 66px; top: 1099px; font-size: 17px; line-height: 25.5px; letter-spacing: 0.6px; }

  .level-visual {
    position: absolute; left: 582px; top: 923px; width: 226px; height: 245px;
    border-radius: 50%;
    background: radial-gradient(circle at 50% 50%, rgba(196,122,58,0.6), rgba(40,40,40,0.3) 65%, rgba(40,40,40,0) 71%);
  }
</style>
</head>
<body>
<main class="certificate">
  <div class="band band--top" role="img" aria-label="Decorative teal wave artwork"></div>

  <div class="brand-seal">
    <span class="brand-seal__name">Fascial<br>Balance<br>Method</span>
  </div>

  <div class="title-ribbon">
    <svg viewBox="0 0 497 67" preserveAspectRatio="none" aria-hidden="true">
      <polygon points="0,0 497,0 477,33.5 497,67 0,67 20,33.5" fill="var(--gold)"/>
    </svg>
    <h1>CERTIFICATE</h1>
  </div>

  <section class="recipient">
    <p class="recipient__name">Tomas Herrera</p>
    <p class="recipient__course">has completed the fasciatherapy level I course<br>- 3 days, 75-77 february 2020 -<br>Kópavogur, Iceland 77 february 2020.</p>
  </section>

  <p class="signatory signatory--left">Mr. JK van Dam<br>Co-Director</p>
  <p class="signatory signatory--right">Mr. RT Lindqvist<br>Co-Director</p>

  <p class="registration">Registration number: 4 KOP 20</p>
  <p class="terms">The Fascial Balance Method ongoing certification is contingent<br>upon meeting the requirements of the maintenance of the<br>certification of Fasciatherapy</p>

  <address class="issuer">Myofascia Works BV<br>Eerste Lindengracht 14<br>1015KL Amsterdam<br>The Netherlands</address>

  <div class="band band--bottom" role="img" aria-label="Decorative gold and orange wave artwork"></div>

  <p class="tagline">Specialists in<br>fasciatherapy<br>innovation</p>

  <div class="level-visual" role="img" aria-label="Wooden tensegrity structure of struts and cables marking the course level"></div>
</main>
</body>
</html>
```